Redesign Website for Tandara Flame

I have an existing website on https://www.tandaraflame-example.com.au/ and would like to have this redesigned professionally with new content (please refer to word document). We are fire protection engineers providing fire services design expertise and engineering design to a range of different clients.

We also provide drafting services to clients in the form of completing final commissioning documentation such as 'as-installed' drawings and fire services block plans to ensure compliance with the building code and relevant Australian Standards.

Target Market(s)

Builders, Architects, Consultants, Project Managers

Industry/Entity Type

Engineering Consultant

Coding

Coded - Design and coding required

Number of Pages Required

4 page

Font styles to use
Sans Serif

Requirements
Must have
• Home and about Page, fire services design page, fire block plans page, contact us page (4 Pages).

The website colour choice must match or compliment the new company logo.
Nice to have
• Quality photos of fire services installations in buildings to Australian Standards.

A website similar to this would be ideal http://corbellpyro-example.com.au
Should not have
• Stolen licensed photos

```html
<!DOCTYPE html>
<html lang="en">
<head>
<meta charset="utf-8">
<title>Tandara Flame — Fire Services Design</title>
<link rel="stylesheet" href="https://fonts.googleapis.com/css2?family=Montserrat:wght@300;400;500;600;700&display=swap">
<style>
:root{
  --orange:#f7941d;
  --orange-soft:#fde3c4;
  --cream:#fdf6ee;
  --grey-bg:#f2f3f6;
  --navy:#1c2b4f;
  --ink:#1e1e1e;
  --body:#7a7a7a;
  --white:#ffffff;
}
*{box-sizing:border-box;margin:0;padding:0}
html,body{width:1200px;height:3125px;overflow:hidden}
body{position:relative;background:var(--white);font-family:"Montserrat",Arial,sans-serif;color:var(--ink)}
.abs{position:absolute}
.backdrop{position:absolute;left:0;top:0;width:1200px;height:3125px}
.center{left:0;width:1200px;text-align:center}

.brand-top{top:100px}
.brand-top .dot{display:block;width:44px;height:44px;border-radius:50%;border:3px solid var(--orange);margin:0 auto 10px}
.brand-top .name{font-size:24px;font-weight:600;color:var(--orange);letter-spacing:.5px}

.hero-photo{left:174px;top:185px;width:839px;height:446px;
  background:linear-gradient(160deg,#6b6658 0%,#8c8576 35%,#5a5a55 60%,#3d3d3c 100%);
  clip-path:polygon(0 0,100% 0,100% 86.5%,50% 100%,0 88%)}
.hero-shade{left:174px;top:185px;width:839px;height:446px;background:rgba(0,0,0,.28);
  clip-path:polygon(0 0,100% 0,100% 86.5%,50% 100%,0 88%)}
.nav a{position:absolute;top:206px;font-size:8.5px;font-weight:600;color:var(--white);letter-spacing:.8px;text-decoration:none;text-transform:uppercase}
.nav-brand{top:196px;left:0;width:1186px;text-align:center;color:var(--white)}
.nav-brand .dot{display:block;width:22px;height:22px;border-radius:50%;border:2px solid var(--white);margin:0 auto 4px}
.nav-brand .name{font-size:11px;font-weight:600}
.hero-title{top:328px;font-size:31px;font-weight:700;line-height:36px;color:var(--white);text-transform:uppercase}
.hero-text{top:412px;left:362px;width:462px;font-size:10.5px;line-height:15px;color:#f4f4f4;text-align:center}
.btn{position:absolute;height:34px;background:var(--orange);color:var(--white);font-size:8.5px;font-weight:600;letter-spacing:.6px;text-transform:uppercase;display:flex;align-items:center;justify-content:center;gap:10px}
.btn::after{content:"›";font-size:13px;line-height:1}
.scroll-btn{left:576px;top:626px;width:34px;height:34px;border-radius:50%;background:var(--white);box-shadow:0 2px 8px rgba(0,0,0,.15);display:flex;align-items:center;justify-content:center;font-size:12px;color:var(--ink)}

.section-title{font-size:28px;font-weight:300;letter-spacing:.5px;text-transform:uppercase}
.section-title b{font-weight:700}
.divider{left:486px;width:216px;height:12px}
.divider::before,.divider::after{content:"";position:absolute;top:6px;width:84px;height:1px;background:var(--orange)}
.divider::before{left:0}.divider::after{right:0}
.divider span{position:absolute;left:100px;top:0;width:12px;height:12px;border-radius:50%;border:1.5px solid var(--orange)}
.body-text{font-size:10px;line-height:14.6px;color:var(--body);text-align:center}

.service .icon{position:absolute;width:40px;height:40px;border-radius:50%;background:var(--orange-soft)}
.service h4{position:absolute;width:170px;text-align:center;font-size:10px;font-weight:600;line-height:12.5px;color:var(--ink)}
.service p{position:absolute;width:150px;text-align:center;font-size:9px;line-height:14px;color:var(--body)}
.hub{left:500px;top:1240px;width:186px;height:186px;border-radius:50%;background:var(--white);box-shadow:0 10px 30px rgba(0,0,0,.12);border:14px solid var(--orange);display:flex;align-items:center;justify-content:center;font-size:17px;font-weight:600;color:var(--orange);text-align:center}

.photo{position:absolute}
.label{position:absolute;font-size:8px;font-weight:600;color:var(--orange);letter-spacing:1.5px;text-transform:uppercase;padding-left:26px}
.label::before{content:"";position:absolute;left:0;top:4px;width:20px;height:1px;background:var(--orange)}
.heading{position:absolute;font-size:24px;font-weight:300;line-height:29px}
.heading b{font-weight:700}
.checks{left:606px;top:1940px;width:300px;display:grid;grid-template-columns:134px 140px;row-gap:9px;font-size:9px;line-height:13px;color:#444}
.checks li{list-style:none;position:relative;padding-left:19px;min-height:26px}
.checks li::before{content:"✓";position:absolute;left:0;top:0;width:12px;height:12px;border-radius:50%;background:var(--orange);color:var(--white);font-size:8px;line-height:12px;text-align:center}

.card{position:absolute;top:2328px;height:262px;background:var(--white);box-shadow:0 6px 20px rgba(0,0,0,.08);overflow:hidden}
.card .shot{height:144px}
.card .cat{position:absolute;left:16px;top:165px;font-size:7.5px;color:var(--body)}
.card h5{position:absolute;left:16px;top:176px;font-size:10px;font-weight:600;white-space:nowrap}
.card p{position:absolute;left:16px;top:199px;width:150px;font-size:9px;line-height:15px;color:var(--body);white-space:nowrap}
.mini{position:absolute;width:26px;height:26px;border-radius:50%;background:var(--white);box-shadow:0 2px 6px rgba(0,0,0,.18);display:flex;align-items:center;justify-content:center;font-size:11px;color:var(--ink)}
.mini.on{background:var(--orange);color:var(--white)}
.next{left:860px;top:2415px;width:70px;height:70px;border-radius:50%;background:var(--white);box-shadow:0 4px 14px rgba(0,0,0,.15);display:flex;align-items:center;justify-content:center;color:var(--orange);font-size:22px}

.field{position:absolute;height:31px;border:1px solid rgba(255,255,255,.45);font-size:8.5px;color:rgba(255,255,255,.7);padding:11px 9px}
</style>
</head>
<body>

<svg class="backdrop" viewBox="0 0 1200 3125" aria-hidden="true">
  <polygon points="174,734 593,661 1013,734 1013,1008 174,1008" fill="#fdf6ee"/>
  <polygon points="174,572 593,628 1013,570 1013,584 593,656 174,586" fill="#f7941d"/>
  <polygon points="174,1720 593,1631 1013,1710 1013,2274 174,2274" fill="#f2f3f6"/>
  <polygon points="174,1712 593,1621 1013,1702 1013,1712 593,1633 174,1722" fill="#f7941d"/>
  <polygon points="174,2644 1013,2644 1013,3045 593,3100 174,3045" fill="#1c2b4f"/>
  <polygon points="174,3045 593,3100 1013,3045 1013,3058 593,3125 174,3058" fill="#f7941d"/>
  <g stroke="#f7941d" stroke-width="1" stroke-dasharray="2,3" fill="none">
    <polyline points="414,1199 454,1199 522,1274"/>
    <polyline points="786,1201 746,1201 666,1274"/>
    <polyline points="414,1471 454,1471 522,1394"/>
    <polyline points="786,1471 746,1471 666,1394"/>
  </g>
  <g fill="#f7941d">
    <circle cx="414" cy="1199" r="2.5"/><circle cx="786" cy="1201" r="2.5"/>
    <circle cx="414" cy="1471" r="2.5"/><circle cx="786" cy="1471" r="2.5"/>
  </g>
</svg>

<header class="abs center brand-top"><span class="dot"></span><span class="name">TANDARA FLAME</span></header>

<section class="hero">
  <div class="abs hero-photo" role="img" aria-label="Photograph of a warehouse building exterior with loading bay doors and concrete driveway"></div>
  <div class="abs hero-shade"></div>
  <nav class="nav">
    <a style="left:302px">Home</a>
    <a style="left:378px">Fire Service</a>
    <a style="left:718px">Fire Block Plan</a>
    <a style="left:834px">Contact Us</a>
  </nav>
  <div class="abs nav-brand"><span class="dot"></span><span class="name">TANDARA FLAME</span></div>
  <h1 class="abs center hero-title">Tandara Flame is<br>a company based in Sydney</h1>
  <p class="abs hero-text">Sed non mauris vitae erat consequat auctor eu in elit. Class aptent taciti sociosqu ad litora torquent per conubia nostra, per inceptos himenaeos. Mauris in erat justo. Nullam ac urna eu felis dapibus condimentum sit amet a augue.</p>
  <a class="btn" style="left:547px;top:480px;width:94px">Read more</a>
  <div class="abs scroll-btn">⌄</div>
</section>

<section class="mission">
  <h2 class="abs center section-title" style="top:712px">Our <b>Mission</b></h2>
  <div class="abs divider" style="top:756px"><span></span></div>
  <p class="abs body-text" style="left:338px;top:793px;width:512px">We also provide fire services design peer review and sign-off under the new Fire Services Design (FSD) class of the Fire Protection Accreditation Scheme (FPAS) and the preparation of a Clause 164B objection letter to exempt certain building work on fire safety systems be exempt from compliance with the BCA and relevant standards.</p>
  <p class="abs body-text" style="left:338px;top:868px;width:512px">We strive to exceed our clients expectations in being competitively priced, meeting the project time constraints without the compromise in quality.</p>
  <a class="btn" style="left:547px;top:921px;width:94px">Read more</a>
</section>

<section class="design">
  <h2 class="abs center section-title" style="top:1048px">Fire <b>Services</b> Design</h2>
  <div class="abs divider" style="top:1092px"><span></span></div>
  <p class="abs body-text" style="left:346px;top:1125px;width:496px">We will assist and guide you throughout the fire services design process, whether you are installing a new fire safety system or upgrading an existing system, we will ensure your new or upgraded fire</p>

  <div class="abs hub">Tandara<br>Flame</div>

  <div class="service">
    <div class="icon" role="img" aria-label="Icon of a fire alarm panel" style="left:366px;top:1180px"></div>
    <h4 style="left:299px;top:1234px">Installing a new fire<br>safety system</h4>
    <p style="left:309px;top:1271px">Lorem quis bibendum auctor, nisi elit consequat ipsum, nec sagittis sem nibh id elit.</p>
  </div>
  <div class="service">
    <div class="icon" role="img" aria-label="Icon of an engineer with equipment" style="left:794px;top:1180px"></div>
    <h4 style="left:721px;top:1234px">Upgrading an<br>existing system</h4>
    <p style="left:733px;top:1271px">Lorem quis bibendum auctor, nisi elit consequat ipsum, nec sagittis sem nibh id elit.</p>
  </div>
  <div class="service">
    <div class="icon" role="img" aria-label="Icon of an engineering report document" style="left:364px;top:1451px"></div>
    <h4 style="left:299px;top:1499px">Fire Engineering<br>Reports</h4>
    <p style="left:309px;top:1538px">Lorem quis bibendum auctor, nisi elit consequat ipsum, nec sagittis sem nibh id elit.</p>
  </div>
  <div class="service">
    <div class="icon" role="img" aria-label="Icon of a specialist with gear" style="left:798px;top:1451px"></div>
    <h4 style="left:725px;top:1499px">Fire Engineering<br>Reports</h4>
    <p style="left:733px;top:1538px">Lorem quis bibendum auctor, nisi elit consequat ipsum, nec sagittis sem nibh id elit.</p>
  </div>
</section>

<section class="about">
  <div class="photo" role="img" aria-label="Photograph of a red fire hydrant valve on a wall" style="left:174px;top:1758px;width:134px;height:145px;background:linear-gradient(135deg,#d9dadb,#b8302c 55%,#c9c9c7)"></div>
  <div class="photo" role="img" aria-label="Photograph of a building interior ceiling with lighting and pipework" style="left:342px;top:1812px;width:216px;height:278px;background:linear-gradient(180deg,#3f4246,#8a8d90 55%,#5a5c5e)"></div>
  <div class="photo" role="img" aria-label="Photograph of a booster connection with red valves against a brick wall" style="left:174px;top:1994px;width:230px;height:199px;border:8px solid #fff;border-left:0;border-top-width:6px;background:linear-gradient(135deg,#6e4433,#8a5a44 50%,#b43a34 75%,#9b9fa2)"></div>

  <div class="label" style="left:600px;top:1783px">About Us</div>
  <h3 class="heading" style="left:599px;top:1803px">Fire Services<br><b>Design &amp; Specifications</b></h3>
  <p class="abs" style="left:600px;top:1875px;width:260px;font-size:9.5px;line-height:15px;color:var(--body)">We have proficient knowledge and capabilities in the preparation of fire services design and specifications relating to the below fire safety systems:</p>
  <ul class="abs checks">
    <li>Smoke Alarms</li><li>Automatic Smoke Detection &amp; Alarm Systems</li>
    <li>Occupant Warning Systems</li><li>Fire Hose Reels</li>
    <li>Fire Hydrants</li><li>Portable Fire Extinguishers</li>
    <li>Emergency Lighting</li><li>Exit Signs</li>
  </ul>
  <a class="btn" style="left:600px;top:2089px;width:94px">Read more</a>
</section>

<section class="projects">
  <div class="label" style="left:304px;top:2366px">Projects</div>
  <h3 class="heading" style="left:303px;top:2384px">Our Recent<br><b>Projects</b></h3>
  <p class="abs" style="left:304px;top:2458px;width:170px;font-size:9px;line-height:14.5px;color:var(--body)">Nam nec tellus a odio tincidunt auctor a ornare odio. Sed non mauris vitae erat consequat auctor eu in elit.</p>
  <a class="btn" style="left:304px;top:2523px;width:114px">See all projects</a>

  <article class="card" style="left:503px;width:183px">
    <div class="shot" role="img" aria-label="Photograph of an underground car park with ceiling pipework" style="background:linear-gradient(180deg,#8d8f90,#c9c7bd 60%,#d2b13c)"></div>
    <span class="cat">Private Residence</span><h5>Ridgeline Retreat</h5>
    <p>Morbi accumsan ipsum velit. Nam<br>nec tellus a odio tincidunt ....</p>
  </article>
  <article class="card" style="left:702px;width:182px">
    <div class="shot" role="img" aria-label="Photograph of red fire valves mounted on a white wall" style="background:linear-gradient(135deg,#e6e6e4,#c2c3c2 50%,#b9403a 80%,#d6d6d4)"></div>
    <span class="cat">Private Residence</span><h5>Crestview Terrace</h5>
    <p>Morbi accumsan ipsum velit. Nam<br>nec tellus a odio tincidunt ....</p>
  </article>
  <article class="card" style="left:901px;width:112px">
    <div class="shot" role="img" aria-label="Photograph of a red fire pump room" style="background:linear-gradient(135deg,#a63028,#c9453a 50%,#7b7f82)"></div>
    <span class="cat">Cold/Freezer Storage</span><h5>Baymoor Storage</h5>
    <p>Morbi accumsan ipsum velit. Nam<br>nec tellus a odio tincidunt ....</p>
  </article>
  <span class="mini on" style="left:584px;top:2563px">›</span>
  <span class="mini" style="left:783px;top:2563px">›</span>
  <span class="mini" style="left:982px;top:2563px">›</span>
  <div class="abs next">→</div>
</section>

<section class="contact">
  <div class="photo" role="img" aria-label="Photograph of a white building corridor with downlights and an exit sign" style="left:304px;top:2698px;width:249px;height:315px;background:linear-gradient(180deg,#cfcbc3,#eeece7 40%,#a9a59d 75%,#d8d5ce)"></div>
  <div class="label" style="left:601px;top:2713px">Contact Us</div>
  <h3 class="heading" style="left:601px;top:2730px;color:var(--white)">Get in <b>Contact</b> with Us</h3>
  <div class="field" style="left:601px;top:2780px;width:135px">First name</div>
  <div class="field" style="left:751px;top:2780px;width:134px">Last name</div>
  <div class="field" style="left:601px;top:2822px;width:135px">Email address</div>
  <div class="field" style="left:751px;top:2822px;width:134px">Phone no</div>
  <div class="field" style="left:601px;top:2865px;width:284px;height:84px">Enter text</div>
  <a class="btn" style="left:601px;top:2972px;width:95px">Submit now</a>
</section>

</body>
</html>
```